Restaurant website built on Plimo’s responsive platform- No coding skills needed

We are looking to add to our company's website www.plimoweb.com a new inspiration page that will include examples of sites built using Plimo's platform.
In order to make it relevant, we would like to have multiple choices for every category, one of the categories is “restaurants.”

REQUIREMENTS:
o Build a "fake" restaurant site on Plimo’s responsive platform, no real restaurant information is needed. The site will include:
1. Homepage
• Restaurant header (no logo)
• Paragraph about the restaurant (can be Lorem ipsum)
• Contact details and contact buttons
• Tastr reviews
• Reserve-a-table widget
• Open hours
2. Menu page
• You can use any menu you'd like
• Reserve a table widget
• Photo gallery
3. Footer
• Social Media links
• Map with location of restaurant

* Order of the elements is up to the designer
* Designer may add more elements as they see fit
* Designer may alter elements from page to page
* Designer will define the site color pallet and text style

****Learn more on how to create a website on Plimo's platform here
https://clipzen.example/584203117

INSTRUCTIONS FOR THIS PROJECT:
Register for a 30-day free trial for Pro access to the platform:
http://www.plimoweb.com/plimopro?_pw_referral=GrfHub

a. After registering, access the dashboard and click on “Create Responsive Website.”
b. Choose a template
c. Start editing! .
d. No need to publish. When ready, take a screenshot of the preview and submit the screenshot to this GraphicHub project. Include the URL/Link to the preview within the submission description.
e. For more information on Plimo, visit the support page at https://support.plimoweb.com/02PlimoOne/Quick_Guide OR call our Support line Mon.-Fri., 9AM-9PM ET.1-866-555-0193

DESIGN PREFERENCES
freestyle (not related to the Plimo brand)

DESIGN SAMPLES (for inspiration)
http://www.plimoweb.com/responsive-website/templates

What not to include in the design -
no restrictions

DELIVERABLES:
* Website on Plimo (No PSD. No coding needed)
* Screenshot preview to GraphicHub with URL/link to your site’s preview.

ABOUT THE COMPANY:
Plimo is a website builder based in California that allow designers, web designers and practically anyone to build its own site. No development and/or technical skills required.

NOTE:
* Plimo is an external site and is not part of GraphicHub
* Please refer to Plimo's Terms and Conditions for information regarding how submissions will be handled (http://www.plimoweb.com/legal/terms)

Target Market(s)

SMBs and web designers that want to create simple, professional and beautiful websites

Industry/Entity Type

Restaurant

Number of Pages Required

2 page

Requirements
Must have
• Please send a preview of the site you created on Plimo, NOT a PSD/JPEG
Should not have
• No coding skills are needed- any web designer can build a site on Plimo

```html
<!DOCTYPE html>
<html lang="en">
<head>
<meta charset="utf-8">
<title>Menu</title>
<link href="https://fonts.googleapis.com/css2?family=Oswald:wght@400&family=Roboto:wght@500;700&display=swap" rel="stylesheet">
<style>
  :root {
    --page: #ffffff;
    --sheet: #efefef;
    --ink: #141414;
    --muted: #585858;
    --price: #4a4a4a;
    --accent: #c8312f;
    --rule: #a9a9a9;
    --footer: #1b1b1b;
    --footer-ink: #ffffff;
  }
  * { box-sizing: border-box; margin: 0; padding: 0; }
  html, body { width: 1200px; height: 900px; overflow: hidden; background: var(--page); }
  body { position: relative; font-family: "Roboto", Arial, sans-serif; }

  .menu-sheet {
    position: absolute; left: 19px; top: 0; width: 1161px; height: 800px;
    background: var(--sheet);
  }
  .menu-section { position: absolute; left: 193px; width: 775px; }
  .section-title {
    font-family: "Oswald", "Arial Narrow", sans-serif;
    font-weight: 400; font-size: 27px; line-height: 33px; color: var(--ink);
    height: 36px; border-bottom: 2px solid var(--accent);
    letter-spacing: -0.2px;
  }
  .section-title.is-hidden { height: 2px; font-size: 0; }
  .section-title + .section-shade {
    height: 8px; margin: 0 -75px;
    background: linear-gradient(to bottom, rgba(0,0,0,0.035), rgba(0,0,0,0));
  }
  .dish-grid { display: flex; justify-content: space-between; padding-top: 26px; }
  .dish-column { width: 375px; }
  .dish {
    display: flex; justify-content: space-between; align-items: flex-start;
    padding-bottom: 11px; border-bottom: 1px solid var(--rule);
    margin-bottom: 13px;
  }
  .dish-text { width: 300px; font-size: 13px; line-height: 15.5px; }
  .dish-name { font-weight: 700; color: var(--ink); }
  .dish-desc { font-weight: 500; color: var(--muted); }
  .dish-price { font-weight: 700; font-size: 13px; line-height: 15.5px; color: var(--price); }

  .site-footer {
    position: absolute; left: 19px; top: 800px; width: 1161px; height: 100px;
    background: var(--footer);
  }
  .social-links { position: absolute; left: 512px; top: 37px; }
</style>
</head>
<body>
  <main class="menu-sheet">
    <section class="menu-section" style="top:4px">
      <h2 class="section-title is-hidden">Entrées</h2>
      <div class="dish-grid" style="padding-top:33px">
        <div class="dish-column">
          <article class="dish">
            <div class="dish-text"><p class="dish-name">Grilled Hanger Steak</p><p class="dish-desc">Served with a mushroom marsala sauce, seasonal veggies, and mashed potato</p></div>
            <span class="dish-price">$16.99</span>
          </article>
          <article class="dish">
            <div class="dish-text"><p class="dish-name">Shrimp a la Spinach</p><p class="dish-desc">Served over warm spinach salad with mushrooms, sundried tomato and blue cheese vinaigrette.</p></div>
            <span class="dish-price">$15.99</span>
          </article>
        </div>
        <div class="dish-column">
          <article class="dish">
            <div class="dish-text"><p class="dish-name">Flounder Franchese</p><p class="dish-desc">Fillet of flounder in a lemon butter white wine sauce served with grilled asparagus.</p></div>
            <span class="dish-price">$15.99</span>
          </article>
        </div>
      </div>
    </section>

    <section class="menu-section" style="top:224px">
      <h2 class="section-title">Sushi</h2>
      <div class="dish-grid">
        <div class="dish-column">
          <article class="dish">
            <div class="dish-text"><p class="dish-name">Sushi Two Roll Special</p><p class="dish-desc">2 Rolls of Your Choice of: Spicy Tuna, California, Cucumber, Avocado, Spicy Salmon, Eel, Tuna, Crab, Salmon or Spicy Crab (Served with Miso Soup and Ginger Salad) (no substitutions)</p></div>
            <span class="dish-price">$8.99</span>
          </article>
        </div>
        <div class="dish-column">
          <article class="dish">
            <div class="dish-text"><p class="dish-name">Jackpot Roll</p><p class="dish-desc">Crab, avocado, cucumber inside, toppped with seared salmon, crunch with spicy mayo and eel sauce.</p></div>
            <span class="dish-price">$13.99</span>
          </article>
        </div>
      </div>
    </section>

    <section class="menu-section" style="top:441px">
      <h2 class="section-title">Dinner Specials</h2>
      <div class="dish-grid">
        <div class="dish-column">
          <article class="dish">
            <div class="dish-text"><p class="dish-name">Lobster &amp; Avocado Salad</p><p class="dish-desc">Grilled lobster, avocado, cherry tomatoes, roasted peppers, red onion and arugula with a citrus vinaigrette.</p></div>
            <span class="dish-price">$13.99</span>
          </article>
        </div>
        <div class="dish-column">
          <article class="dish">
            <div class="dish-text"><p class="dish-name">Hot Crab Dip</p><p class="dish-desc">Baked lump crab meat and Monterey Jack cheese served with toasted crostini.</p></div>
            <span class="dish-price">$12.99</span>
          </article>
        </div>
      </div>
    </section>

    <section class="menu-section" style="top:642px">
      <h2 class="section-title">Pasta</h2>
      <div class="dish-grid">
        <div class="dish-column">
          <article class="dish">
            <div class="dish-text"><p class="dish-name">Cavatelli Caprese</p><p class="dish-desc">Ricotta cavatelli with grilled chicken, tomato, roasted peppers, and asparagus in a shallot white win sauce topped with melted mozzarella.</p></div>
            <span class="dish-price">$23.99</span>
          </article>
        </div>
        <div class="dish-column">
          <article class="dish">
            <div class="dish-text"><p class="dish-name">Scallop &amp; Shrimp Pappardelle</p><p class="dish-desc">Fresh wide noodles with scallops, shrimp, shittake mushrooms, diced tomatoes, and arugula in a garlic and white wine sauce.</p></div>
            <span class="dish-price">$26.99</span>
          </article>
        </div>
      </div>
    </section>
  </main>

  <footer class="site-footer">
    <svg class="social-links" width="160" height="36" viewBox="0 0 160 36" aria-label="Social media links">
      <circle cx="18" cy="18" r="17" fill="none" stroke="var(--footer-ink)" stroke-width="2"/>
      <circle cx="68" cy="18" r="17" fill="none" stroke="var(--footer-ink)" stroke-width="2"/>
      <circle cx="118" cy="18" r="17" fill="none" stroke="var(--footer-ink)" stroke-width="2"/>
    </svg>
  </footer>
</body>
</html>
```